Computer Repair Business - Needs New Business Card Design

I want to create a very cool business card for my business. I want to make it 100% different from my previous card. I would like to use similar color scheme like Royal blue.

With this card I want to create a conversation and have my customers say "Wow, that's a cool business card" Trying to prevent it from looking like the typical card that get's shoved into a wallet.

My website is below:

www.milospcworks.com

I want to edit the hours and website and email:

www.milospcworks.com
milo@milospcworks.com

10:30 to 6pm Monday - Friday
10:30 to 3pm Saturday

Just to remind, when i see a new design i don't want to notice my old design.

Business card will be printed and made with rounded corners and horizontal.

The back of the card should say " In-Store Repair, Remote Support, Data Recovery"

Industry/Entity Type

Business

Font styles to use
Sans Serif

Colors
33a6d7
3176b5

Requirements
Must have
• Clean looking - have creative aspects.
Should not have
• Should not look like the previous card design.

```html
<!DOCTYPE html>
<html lang="en">
<head>
<meta charset="utf-8">
<title>Milo's PC Works – Business Card</title>
<link rel="stylesheet" href="https://fonts.googleapis.com/css2?family=PT+Sans:ital,wght@0,400;0,700;1,400&family=PT+Sans+Narrow:wght@700&display=swap">
<style>
  :root {
    --page-bg: #e6e6e6;
    --card-black: #1d1d1d;
    --card-black-light: #3a3a3a;
    --screen-white: #ffffff;
    --bar-grey: #ececec;
    --field-white: #ffffff;
    --royal-blue: #2455a8;
    --icon-blue: #3176b5;
    --icon-light: #33a6d7;
    --silver: #d6d6d6;
    --badge-grey: #5a5a5a;
    --lock-green: #5aa832;
    --menu-red: #d9332b;
  }
  * { box-sizing: border-box; margin: 0; padding: 0; }
  html, body { width: 1000px; height: 1200px; overflow: hidden; }
  body {
    background: var(--page-bg);
    font-family: "PT Sans", Arial, sans-serif;
    position: relative;
  }

  .card {
    position: absolute;
    left: 80px;
    width: 840px;
    height: 490px;
    border-radius: 34px;
    background: linear-gradient(160deg, var(--card-black-light) 0%, var(--card-black) 45%, #111 100%);
    box-shadow: 0 10px 30px rgba(0,0,0,.25);
  }
  .card--front { top: 60px; }
  .card--back { top: 640px; }

  /* front: device frame */
  .camera {
    position: absolute; top: 26px; left: 50%; width: 30px; height: 30px; margin-left: -15px;
    border-radius: 50%; background: #0b0b0b; border: 3px solid #555;
  }
  .sensor {
    position: absolute; top: 38px; width: 6px; height: 6px; border-radius: 50%;
    border: 1px solid #666;
  }
  .sensor--left { left: 370px; }
  .sensor--right { left: 466px; }

  .screen {
    position: absolute; top: 80px; left: 80px; right: 50px; bottom: 70px;
    background: var(--screen-white); border-radius: 10px; overflow: hidden;
  }
  .browser-bar {
    height: 52px; background: var(--bar-grey); display: flex; align-items: center;
    padding: 0 12px; gap: 10px;
  }
  .browser-bar svg { flex: none; }
  .address-field {
    flex: 1; height: 38px; background: var(--field-white); border-radius: 6px;
    display: flex; align-items: center; gap: 10px; padding: 0 12px;
    font-size: 21px; color: #222;
  }
  .address-field .url { flex: 1; }

  .screen-body { position: relative; padding: 18px 28px; height: 288px; }
  .services-title { font-size: 30px; font-weight: 700; color: var(--royal-blue); line-height: 1.1; }
  .phone { font-size: 26px; font-style: italic; color: var(--royal-blue); line-height: 1.1; }
  .contact-line { font-size: 21px; color: var(--royal-blue); line-height: 1.2; }
  .divider { width: 270px; height: 3px; background: var(--royal-blue); margin: 14px 0 10px; }
  .hours-title { font-size: 26px; font-weight: 700; color: var(--royal-blue); line-height: 1.1; }
  .hours-line { font-size: 21px; color: var(--royal-blue); line-height: 1.15; white-space: nowrap; }

  .feature-list { position: absolute; top: 14px; right: 22px; width: 220px; list-style: none; }
  .feature {
    display: flex; align-items: center; gap: 14px; height: 88px;
  }
  .feature-icon {
    width: 58px; height: 50px; flex: none; border-radius: 6px;
    background: linear-gradient(135deg, var(--icon-light), var(--icon-blue));
  }
  .feature-label {
    font-family: "PT Sans Narrow", "Arial Narrow", sans-serif;
    font-weight: 700; text-transform: uppercase;
    font-size: 19px; line-height: 1.1; color: var(--royal-blue);
  }

  .partner-badge {
    position: absolute; bottom: 24px; left: 50%; width: 180px; height: 20px; margin-left: -90px;
    border-radius: 4px; background: var(--badge-grey);
  }

  /* back */
  .brand {
    position: absolute; top: 50%; left: 50%; transform: translate(-50%, -50%);
    display: flex; flex-direction: column; align-items: center; gap: 22px;
  }
  .brand-lockup { display: flex; align-items: center; gap: 18px; }
  .brand-mark { width: 46px; height: 46px; background: var(--silver); }
  .brand-name {
    font-size: 50px; font-weight: 700; color: var(--silver); letter-spacing: 2px;
    white-space: nowrap; line-height: 1;
  }
  .brand-services {
    font-size: 20px; color: var(--icon-light); letter-spacing: 1.5px; white-space: nowrap;
  }
</style>
</head>
<body>

<section class="card card--front" aria-label="Card front">
  <span class="sensor sensor--left"></span>
  <span class="camera"></span>
  <span class="sensor sensor--right"></span>

  <div class="screen">
    <div class="browser-bar">
      <svg width="96" height="26" viewBox="0 0 96 26" aria-hidden="true" fill="none" stroke="#222" stroke-width="2.6" stroke-linecap="round" stroke-linejoin="round">
        <path d="M22 13H4M12 5 4 13l8 8"/>
        <path d="M38 13h18M48 5l8 8-8 8"/>
        <path d="M72 5l16 16M88 5 72 21"/>
      </svg>
      <div class="address-field">
        <svg width="14" height="18" viewBox="0 0 14 18" aria-hidden="true">
          <path d="M3 8V5a4 4 0 0 1 8 0v3" fill="none" stroke="var(--lock-green)" stroke-width="2"/>
          <rect x="1" y="8" width="12" height="9" rx="1.5" fill="var(--lock-green)"/>
        </svg>
        <span class="url">www.milospcworks.com</span>
        <svg width="26" height="26" viewBox="0 0 24 24" aria-hidden="true">
          <path d="M12 2l3 6.5 7 .8-5.2 4.8 1.4 7-6.2-3.5-6.2 3.5 1.4-7L2 9.3l7-.8z" fill="none" stroke="#555" stroke-width="1.5" stroke-linejoin="round"/>
        </svg>
      </div>
      <svg width="14" height="18" viewBox="0 0 14 18" aria-hidden="true" fill="var(--menu-red)">
        <rect y="2" width="14" height="3"/><rect y="8" width="14" height="3"/><rect y="14" width="14" height="3"/>
      </svg>
    </div>

    <div class="screen-body">
      <h1 class="services-title">Computer Repair &nbsp;/&nbsp; Sales</h1>
      <p class="phone">555.214.0387</p>
      <p class="contact-line">milo@milospcworks.com</p>
      <p class="contact-line">72 Orchard Lane, Millbrook, NJ 07999</p>
      <div class="divider"></div>
      <h2 class="hours-title">Hours</h2>
      <p class="hours-line">Mon - Fri 10:30 am - 6:00 pm</p>
      <p class="hours-line">Sat 10:30 am - 3:00 pm</p>
      <p class="hours-line">After hours support available by appointment</p>

      <ul class="feature-list">
        <li class="feature">
          <span class="feature-icon" role="img" aria-label="Screwdriver illustration"></span>
          <span class="feature-label">In-Store<br>Computer<br>Services</span>
        </li>
        <li class="feature">
          <span class="feature-icon" role="img" aria-label="Globe support illustration"></span>
          <span class="feature-label">On-Site<br>Support</span>
        </li>
        <li class="feature">
          <span class="feature-icon" role="img" aria-label="Processor chip illustration"></span>
          <span class="feature-label">Computers,<br>Parts, and<br>Accessories</span>
        </li>
      </ul>
    </div>
  </div>

  <span class="partner-badge" aria-hidden="true"></span>
</section>

<section class="card card--back" aria-label="Card back">
  <div class="brand">
    <div class="brand-lockup">
      <span class="brand-mark" aria-hidden="true"></span>
      <span class="brand-name">MILO'S PC WORKS</span>
    </div>
    <p class="brand-services">In-Store Repair, Remote Support, Data Recovery</p>
  </div>
</section>

</body>
</html>
```